Bref créative
Brightwave IT Business cards
Professional
Kenneth Darrow
Chief Information Officer
248 Maple Hollow Rd
KDarrow@BrightwaveIT.example
www.brightwaveit.example
IT managed services
Managed backups
Web Hosting
Email Hosting
Spam Filtering
Networking
Structured Cabling
Project Planning
Colocation Services

```html
<!DOCTYPE html>
<html lang="en">
<head>
<meta charset="utf-8">
<title>Brightwave IT – Business Cards</title>
<link rel="stylesheet" href="https://fonts.googleapis.com/css2?family=Open+Sans:ital,wght@0,400;0,600;0,700;1,400&display=swap">
<style>
  :root {
    --page: #ffffff;
    --brand-blue: #1f6fc0;
    --brand-blue-dark: #1a4f8f;
    --swoosh-blue: #2a86d6;
    --grey-light: #f1f2f4;
    --grey-mid: #d4d6da;
    --grey-deep: #b9bcc2;
    --text-dark: #2f3338;
    --text-grey: #5a5f66;
  }
  * { box-sizing: border-box; margin: 0; padding: 0; }
  html, body {
    width: 1200px; height: 523px; overflow: hidden;
    background: var(--page);
    font-family: "Open Sans", Arial, sans-serif;
  }
  .sheet { position: relative; width: 1200px; height: 523px; }

  .card {
    position: absolute; top: 68px;
    width: 500px; height: 396px;
    overflow: hidden;
    background: var(--page);
    box-shadow: 0 0 0 1px #e2e4e7;
  }
  .card--front { left: 90px; }
  .card--back { left: 612px; }
  .card__art { position: absolute; inset: 0; width: 100%; height: 100%; }

  .brand {
    position: absolute; left: 30px; top: 58px;
    display: flex; align-items: center; gap: 12px;
  }
  .brand__dot {
    width: 38px; height: 38px; border-radius: 50%;
    background: var(--brand-blue);
  }
  .brand__name {
    font-size: 36px; font-weight: 600; letter-spacing: 0.5px;
    color: var(--brand-blue-dark);
  }

  .person { position: absolute; left: 30px; top: 160px; }
  .person__name {
    font-size: 19px; font-weight: 700; color: var(--brand-blue);
  }
  .person__title {
    font-size: 14px; font-style: italic; color: var(--text-grey);
    margin-top: 1px;
  }

  .contact {
    position: absolute; left: 30px; top: 250px;
    font-size: 12.5px; color: var(--text-dark);
    border-collapse: collapse;
  }
  .contact th {
    text-align: left; font-weight: 700; color: var(--brand-blue-dark);
    padding: 1px 6px 1px 0; white-space: nowrap;
  }
  .contact td { padding: 1px 0; white-space: nowrap; }

  .services {
    position: absolute; left: 322px; top: 210px;
    list-style: none; font-size: 12.5px; color: var(--text-dark);
  }
  .services li {
    display: flex; align-items: center; gap: 6px;
    height: 25px;
  }
  .services li::before {
    content: ""; width: 9px; height: 9px; border-radius: 50%;
    background: var(--swoosh-blue);
    box-shadow: inset -2px -2px 0 rgba(0,0,0,0.15);
  }
</style>
</head>
<body>
<main class="sheet">

  <section class="card card--front" aria-label="Business card front">
    <svg class="card__art" viewBox="0 0 500 396" aria-hidden="true">
      <defs>
        <linearGradient id="front-band" x1="0" y1="0" x2="0" y2="1">
          <stop offset="0" stop-color="#e4e6e9"/>
          <stop offset="0.5" stop-color="#d2d5d9"/>
          <stop offset="1" stop-color="#bfc2c7"/>
        </linearGradient>
        <linearGradient id="front-haze" x1="0" y1="0" x2="1" y2="0">
          <stop offset="0" stop-color="#ffffff" stop-opacity="0"/>
          <stop offset="1" stop-color="#e3e5e8"/>
        </linearGradient>
      </defs>
      <rect width="500" height="396" fill="#ffffff"/>
      <path d="M220 0 H500 V160 C420 140 330 120 220 0 Z" fill="url(#front-haze)"/>
      <path d="M0 232 C150 220 340 170 500 92 V396 H0 Z" fill="url(#front-band)"/>
      <path d="M0 250 C160 238 350 190 500 120 V396 H0 Z" fill="#ffffff" opacity="0.18"/>
      <path d="M0 232 C150 220 340 170 500 92" fill="none" stroke="var(--swoosh-blue)" stroke-width="4"/>
      <path d="M0 224 C150 212 330 160 500 80" fill="none" stroke="#ffffff" stroke-width="3" opacity="0.9"/>
    </svg>

    <div class="brand">
      <span class="brand__dot"></span>
      <span class="brand__name">Brightwave IT</span>
    </div>

    <div class="person">
      <p class="person__name">Kenneth Darrow</p>
      <p class="person__title">Chief Information Officer</p>
    </div>

    <table class="contact">
      <tr><th>Address</th><td>: 248 Maple Hollow Rd</td></tr>
      <tr><th>Phone</th><td>: 555-014-2290</td></tr>
      <tr><th>Email</th><td>: KDarrow@BrightwaveIT.example</td></tr>
      <tr><th>Website</th><td>: www.brightwaveit.example</td></tr>
    </table>

    <ul class="services">
      <li>IT managed services</li>
      <li>Managed backups</li>
      <li>Web Hosting</li>
      <li>Email Hosting</li>
      <li>Spam Filtering</li>
      <li>Colocation Services</li>
    </ul>
  </section>

  <section class="card card--back" aria-label="Business card back">
    <svg class="card__art" viewBox="0 0 500 396" aria-hidden="true">
      <defs>
        <linearGradient id="back-side" x1="0" y1="0" x2="1" y2="1">
          <stop offset="0" stop-color="#eceef0"/>
          <stop offset="0.6" stop-color="#d3d6da"/>
          <stop offset="1" stop-color="#bdc0c5"/>
        </linearGradient>
      </defs>
      <rect width="500" height="396" fill="url(#back-side)"/>
      <path d="M60 0 H500 V396 H110 C10 320 -10 120 60 0 Z" fill="#ffffff"/>
      <path d="M60 0 C-10 120 10 320 110 396" fill="none" stroke="var(--swoosh-blue)" stroke-width="5"/>
      <path d="M50 0 C-18 120 0 320 96 396" fill="none" stroke="#ffffff" stroke-width="2" opacity="0.7"/>
    </svg>
  </section>

</main>
</body>
</html>
```